Letterhead and Envelope Design for Investment Company

We need a letterhead and envelope design.
We are a family owned investment company doing direct investments into other family owned businesses.
I have attached all our current marketing material including our logo for reference.

Our under construction website can be found here:
https://rob-darke-qv7m.pagevorlo.com/
password: Copperfen

Target Market(s)

Bankers, business owners, financial partners

Industry/Entity Type

Investment

Colors

Designer to choose colors to be used in the design.

Requirements
Must have
• Logo, and company information

```html
<!DOCTYPE html>
<html lang="en">
<head>
<meta charset="utf-8">
<title>Copperfen Holdings – Letterhead and Envelope</title>
<link href="https://fonts.googleapis.com/css2?family=PT+Serif&family=Heebo:wght@400;500&family=Damion&display=swap" rel="stylesheet">
<style>
  :root{
    --backdrop:#808080;
    --paper:#ffffff;
    --gold:#dcab24;
    --gold-light:#e6bb35;
    --gold-dark:#c99a1a;
    --ink:#1c1c1c;
    --text:#262626;
    --on-gold:#3a2a05;
  }
  *{margin:0;padding:0;box-sizing:border-box}
  html,body{width:1200px;height:900px;overflow:hidden}
  body{
    background:radial-gradient(ellipse at center,#8a8a8a 0%,var(--backdrop) 60%,#707070 100%);
    position:relative;
    font-family:'Heebo',sans-serif;
    color:var(--text);
  }
  .sheet{position:absolute;background:var(--paper);overflow:hidden;box-shadow:0 2px 6px rgba(0,0,0,.25)}
  .letterhead{left:57px;top:102px;width:534px;height:691px}
  .envelope-front{left:670px;top:103px;width:471px;height:235px}
  .envelope-back{left:670px;top:370px;width:471px;height:236px}

  .brand{position:absolute;display:flex;align-items:center;gap:7px;white-space:nowrap}
  .brand-mark{width:10px;height:10px;background:var(--gold);flex:none}
  .brand-name{font-family:'Heebo',sans-serif;font-weight:500;font-size:14px;letter-spacing:.5px;color:var(--ink)}
  .letterhead .brand{left:44px;top:84px}
  .envelope-front .brand{left:21px;top:72px}
  .envelope-front .brand-name{font-size:13px}

  .contact{position:absolute;font-family:'PT Serif',serif;font-size:9.6px;line-height:11.5px;color:var(--text)}
  .letterhead .contact{left:332px;top:43px;padding-left:9px;border-left:1px solid var(--gold)}
  .contact-row{display:flex;align-items:center;gap:4px}
  .contact-row svg{width:10px;height:10px;flex:none}
  .contact .gap{height:5px}
  .envelope-front .contact{right:22px;top:22px;text-align:right}

  .recipient{position:absolute;left:43px;top:197px;font-size:9.2px;line-height:11.5px}
  .recipient-name{font-size:11px;font-weight:500;margin-bottom:4px}

  .body-copy{position:absolute;left:43px;top:268px;width:450px;font-size:9.6px;line-height:15.7px;color:var(--text)}
  .body-copy p+p{margin-top:15.7px}
  .sign-off{position:absolute;left:43px;top:471px;font-size:9.6px}
  .signature{position:absolute;left:43px;top:498px;font-family:'Damion',cursive;font-size:36px;color:var(--ink);line-height:1}
  .signer{position:absolute;left:43px;top:548px;font-size:11px;font-weight:500}

  .swoosh{position:absolute;left:0;bottom:0;width:100%;display:block}
  .web{position:absolute;font-family:'PT Serif',serif;font-size:9.6px;color:var(--on-gold)}
  .letterhead .web{right:45px;top:661px}
  .envelope-front .web{right:22px;top:212px;font-size:8.5px}

  .flap{position:absolute;left:0;top:0;width:471px;height:68px}
  .flap-name{position:absolute;left:0;top:29px;width:471px;text-align:center;font-family:'Heebo',sans-serif;font-weight:500;font-size:11px;letter-spacing:2px;color:var(--ink)}
</style>
</head>
<body>

<section class="sheet letterhead">
  <div class="brand">
    <span class="brand-mark"></span>
    <span class="brand-name">COPPERFEN HOLDINGS INC</span>
  </div>

  <div class="contact">
    <div>48 Mill Row, Suite 210</div>
    <div>Ashford Vale, IA 50917</div>
    <div class="gap"></div>
    <div class="contact-row">
      <svg viewBox="0 0 10 10"><circle cx="5" cy="5" r="4.5" fill="none" stroke="var(--gold)"/><path d="M3.2 2.8h1l.5 1.3-.6.5c.3.7.8 1.2 1.4 1.4l.5-.6 1.3.5v1c-2.6.2-4.3-1.6-4.1-4.1z" fill="var(--gold)"/></svg>
      <span>555 208 6143</span>
    </div>
    <div class="contact-row">
      <svg viewBox="0 0 10 10"><circle cx="5" cy="5" r="4.5" fill="var(--gold)"/><rect x="2.6" y="3.4" width="4.8" height="3.3" fill="#fff"/><path d="M2.6 3.4L5 5.3 7.4 3.4" fill="none" stroke="var(--gold)" stroke-width=".6"/></svg>
      <span>rob.darke@copperfenholdings.com</span>
    </div>
  </div>

  <div class="recipient">
    <div class="recipient-name">MARK ELLISON</div>
    <div>Street Name,City Name.</div>
    <div>Zip Coad 0000</div>
  </div>

  <div class="body-copy">
    <p>Lorem Ipsum is simply dummy text of the printing and typesetting industry. Lorem Ipsum has been the industry's standard dummy text ever since the 1500s, when an unknown printer took a galley of type and scrambled it to make a type specimen book. It has survived not only five centuries,but also the leap into electronic typesetting, remaining essentially unchanged. It was popularised in the 1960s with the release of transfer sheets containing Lorem Ipsum passages, and more recently with desktop publishing software and layout programs including versions of Lorem Ipsum.</p>
    <p>It is a long established fact that a reader will be distracted by the readable content of a page when looking at its layout. The point of using Lorem Ipsum is that it has a more-or-less normal distribution of letters, as opposed to using 'Content here, content here', making it look like readable English. Many desktop and publishing packages and web page editors now use Lorem Ipsum as their default model text, and a search for 'lorem ipsum' will uncover many web sites still in their infancy. Various versions have evolved over the years, sometimes by accident, sometimes on purpose (injected humour and the like).</p>
  </div>
  <div class="sign-off">Regards,</div>
  <div class="signature">Rob Darke</div>
  <div class="signer">Rob Darke</div>

  <svg class="swoosh" viewBox="0 0 534 120" width="534" height="120" aria-hidden="true">
    <path d="M0 96 Q300 102 534 31 L534 120 L0 120 Z" fill="var(--gold)"/>
    <path d="M27 99 Q300 92 534 1 L534 25 Q330 94 27 99 Z" fill="var(--ink)"/>
  </svg>
  <div class="web">www.COPPERFENHOLDINGS.com</div>
</section>

<section class="sheet envelope-front">
  <div class="brand">
    <span class="brand-mark"></span>
    <span class="brand-name">COPPERFEN HOLDINGS INC</span>
  </div>
  <div class="contact">
    <div>48 Mill Row, Suite 210</div>
    <div>Ashford Vale, IA 50917</div>
  </div>
  <svg class="swoosh" viewBox="0 0 471 100" width="471" height="100" aria-hidden="true">
    <path d="M0 90 Q250 96 471 31 L471 100 L0 100 Z" fill="var(--gold)"/>
    <path d="M14 91 Q260 86 471 3 L471 26 Q280 88 14 91 Z" fill="var(--ink)"/>
  </svg>
  <div class="web">www.COPPERFENHOLDINGS.com</div>
</section>

<section class="sheet envelope-back">
  <svg class="flap" viewBox="0 0 471 68" width="471" height="68" aria-hidden="true">
    <defs>
      <linearGradient id="flapGold" x1="0" x2="1" y1="0" y2="0">
        <stop offset="0" stop-color="#c99a1a"/>
        <stop offset=".5" stop-color="#e6bb35"/>
        <stop offset="1" stop-color="#c99a1a"/>
      </linearGradient>
    </defs>
    <path d="M0 0 H471 L463 58 Q462 66 454 66 H17 Q9 66 8 58 Z" fill="url(#flapGold)"/>
  </svg>
  <div class="flap-name">COPPERFEN</div>
</section>

</body>
</html>
```